Business Card Design Project

Hello,

We have just created our new COMPANY LOGO via Pixel Harbor and would not like to turn our attention to new Business Cards.

We are a printing company based in Singapore & Las Vegas. We specialize in blue-print printing for the Architectural, Engineering and Construction industries

The design should be simple, professional, clean and organized.

The Business Cards should "pop" when seen and will hopefully be something that makes you look twice.

We have two different Pan-tones that we use for our company, feel free to use them if you think they will work for your design?

Orange: PMS 021
Gray: PMS 431

I have attached our current logo for your use and reference which should obvious be on our business cards.

Considering we have two locations on different continents, we need business cards templates where the address details need to be interchangeable for each different location (total 2)

First one:
38 Merrow Lane #03-11 to #03-15
Singapore 528473
Tel : +65 6847-3920
Fax : +65 6843-7702

Second one:
2381 W. Tanfield Rd, Suite 204
Las Vegas, Nevada 89152
Tel : (702) 555-4137
Fax : (702) 555-4189

We would also like to list a few of our key services on the card. Here are a few examples to get you going.

Plan Printing & Plotting
Digital Colour Printing
Cadline Printing
Specialty Book Making
Scanning & Archiving
Collection & Delivey

This is the first time i have requested for business cards to be created so please let me know if you require any additional information.
Many Thanks,
Tobin
Updates

Project Deadline Extended
Reason: It took us longer than expected to finalize our Company Logo We look forward to receiving your designs.

Target Market(s)

Our Target Market is construction related people.
Construction
Architecture
Engineering

Industry/Entity Type

Printing

Font styles to use
Other font styles liked:
• Times New Roman

Colors
faa54b
ffffff

Requirements
Must have
• The business card must have our Company Logo (attached)
The font used must be Times New Roman
Should not have
• Playful images of print designs and/or logos

```html
<!DOCTYPE html>
<html lang="en">
<head>
<meta charset="utf-8">
<title>Arden Reprographics – Business Cards</title>
<link href="https://fonts.googleapis.com/css2?family=Tinos:ital,wght@0,400;0,700;1,400;1,700&display=swap" rel="stylesheet">
<style>
  :root{
    --orange:#faa54b;
    --ink:#050505;
    --slate:#333333;
    --paper:#ffffff;
    --mist:#e9eaee;
    --stage:#eeeeec;
  }
  *{box-sizing:border-box;margin:0;padding:0}
  html,body{width:1037px;height:1200px;overflow:hidden;background:var(--stage)}
  body{font-family:"Tinos","Times New Roman",serif;position:relative}
  .card{position:absolute;left:88px;width:860px;height:490px;background:var(--paper);overflow:hidden;box-shadow:0 6px 18px rgba(0,0,0,.18)}
  .card--back{top:70px}
  .card--front{top:640px}
  .card svg.art{position:absolute;inset:0;width:100%;height:100%}
  .services{position:absolute;left:52px;top:104px;list-style:none;color:var(--paper);font-size:21px;line-height:39px}
  .services li{position:relative;padding-left:36px}
  .services li::before{content:"";position:absolute;left:0;top:15px;width:9px;height:9px;border-radius:50%;background:var(--paper)}
  .brand{position:absolute;text-align:center}
  .brand__name{font-weight:700;font-size:46px;letter-spacing:1px;line-height:1}
  .brand__title{font-weight:700;font-size:26px;margin-top:10px}
  .brand__tag{font-style:italic;font-weight:700;font-size:18px;margin-top:4px}
  .card--back .brand{left:380px;top:130px;width:420px;color:var(--paper)}
  .card--front .brand{left:60px;top:62px;width:420px;color:var(--ink)}
  .person{position:absolute;left:40px;top:360px;color:var(--paper)}
  .person__name{font-size:31px;letter-spacing:2px}
  .person__role{font-size:15px;color:#ddd;margin-top:2px}
  .contacts{position:absolute;right:44px;top:320px;list-style:none;color:var(--paper);font-size:19px;text-align:right;line-height:39px}
  .contacts li{display:flex;justify-content:flex-end;align-items:center;gap:14px}
  .contacts svg{width:24px;height:22px;fill:var(--orange)}
</style>
</head>
<body>

<section class="card card--back" aria-label="Card back">
  <svg class="art" viewBox="0 0 860 490" preserveAspectRatio="none" aria-hidden="true">
    <path fill="var(--orange)" d="M0 0H860V0C880 260 760 420 520 440C330 455 160 445 0 440Z"/>
    <path fill="var(--ink)" d="M0 0H800C860 120 830 330 600 395C430 430 200 420 0 410Z"/>
  </svg>
  <ul class="services">
    <li>Plan Printing &amp; Plotting</li>
    <li>Digital Colour Printing</li>
    <li>Cadline Printing</li>
    <li>Specialty Book Making</li>
    <li>Scanning &amp; Archiving</li>
    <li>Collection &amp; Delivey</li>
  </ul>
  <div class="brand">
    <div class="brand__name">Arden</div>
    <div class="brand__title">Arden Reprographics</div>
    <div class="brand__tag">A Member of the Arden Group of Companies</div>
  </div>
</section>

<section class="card card--front" aria-label="Card front">
  <svg class="art" viewBox="0 0 860 490" preserveAspectRatio="none" aria-hidden="true">
    <path fill="var(--mist)" d="M0 265C320 250 620 200 860 100V200C600 240 300 262 0 270Z"/>
    <path fill="var(--orange)" d="M0 272C320 262 620 222 860 155V225C600 260 300 285 0 290Z"/>
    <path fill="var(--slate)" d="M0 290C300 285 600 262 860 225V490H0Z"/>
  </svg>
  <div class="brand">
    <div class="brand__name">Arden</div>
    <div class="brand__title">Arden Reprographics</div>
    <div class="brand__tag">A Member of the Arden Group of Companies</div>
  </div>
  <div class="person">
    <div class="person__name">CORIN VALE</div>
    <div class="person__role">Managing Director</div>
  </div>
  <ul class="contacts">
    <li>(702) 555-4137
      <svg viewBox="0 0 24 22" aria-label="Phone"><path d="M2 6c0-3 4-4 10-4s10 1 10 4v2h-5V6H7v2H2Z"/><path d="M5 10h14l2 10H3Z"/></svg></li>
    <li>(702) 555-4189
      <svg viewBox="0 0 24 22" aria-label="Fax"><rect x="6" y="2" width="12" height="6"/><rect x="2" y="8" width="20" height="9" rx="2"/><rect x="6" y="14" width="12" height="6" fill="var(--slate)" stroke="var(--orange)" stroke-width="2"/></svg></li>
    <li>info@ardenrepro.com
      <svg viewBox="0 0 24 22" aria-label="Email"><path d="M1 3h22v16H1Z"/><path d="M2 4l10 8 10-8" fill="none" stroke="var(--slate)" stroke-width="2"/></svg></li>
    <li>2381 W. Tanfield Rd, Suite 204 Las Vegas, Nevada 89152
      <svg viewBox="0 0 24 22" aria-label="Address"><path d="M12 1 1 11h3v10h6v-6h4v6h6V11h3Z"/></svg></li>
  </ul>
</section>

</body>
</html>
```